Business Card Design Project

I need a business card designed with these details on the front along with the logo attached on the front.

Address - 518/ 217 Wendlebury st Thornvale
Website - www.brackenhollowmasonry.com.au
Email - delwyn@brackenhollowmasonry.com.au
Fax - 1900 457 618
Mobile - 0471926038
Telephone - 1300517926
Licence number - 847263k

```html
<!DOCTYPE html>
<html lang="en">
<head>
<meta charset="utf-8">
<title>Bracken Hollow Masonry – Business Card</title>
<link rel="stylesheet" href="https://fonts.googleapis.com/css2?family=Tinos:wght@700&family=Roboto:wght@400&display=swap">
<style>
  :root {
    --page-bg: #e9e6e2;
    --card-dark: #4a2219;
    --card-light: #f4f6f7;
    --brand-brown: #3d1c14;
    --cream: #efe6dc;
    --tile-stone: #d9cbbd;
    --tile-edge: #b9a592;
    --text-dark: #2b2424;
    --rule: #c9c4c0;
    --faint-mark: #e4e6e7;
  }
  * { margin: 0; padding: 0; box-sizing: border-box; }
  html, body { width: 1200px; height: 880px; overflow: hidden; }
  body {
    background: var(--page-bg);
    display: flex;
    align-items: center;
    justify-content: center;
    gap: 40px;
    font-family: "Roboto", Arial, sans-serif;
  }
  .card {
    width: 540px;
    height: 330px;
    position: relative;
    overflow: hidden;
    box-shadow: 0 6px 18px rgba(0,0,0,0.18);
  }

  /* Back of card */
  .card--back { background: var(--card-dark); }
  .card--back .brand {
    position: absolute;
    left: 92px;
    top: 118px;
    display: flex;
    align-items: center;
    gap: 20px;
  }
  .brand-square {
    width: 84px;
    height: 84px;
    background: var(--tile-stone);
    border: 4px solid var(--tile-edge);
    flex: none;
  }
  .card--back .brand-name {
    font-family: "Tinos", "Times New Roman", serif;
    font-weight: 700;
    font-size: 30px;
    line-height: 1.15;
    letter-spacing: 1.5px;
    color: var(--cream);
    text-transform: uppercase;
  }

  /* Front of card */
  .card--front { background: var(--card-light); }
  .faint-mark {
    position: absolute;
    right: 40px;
    top: 120px;
    width: 150px;
    height: 150px;
    border: 14px solid var(--faint-mark);
  }
  .card--front .brand {
    position: absolute;
    left: 30px;
    top: 26px;
    display: flex;
    align-items: center;
    gap: 12px;
  }
  .card--front .brand-square {
    width: 46px;
    height: 46px;
    border-width: 3px;
  }
  .card--front .brand-name {
    font-family: "Tinos", "Times New Roman", serif;
    font-weight: 700;
    font-size: 17px;
    line-height: 1.15;
    letter-spacing: 0.8px;
    color: var(--brand-brown);
    text-transform: uppercase;
  }
  .contact {
    position: absolute;
    left: 30px;
    top: 100px;
    width: 300px;
    list-style: none;
    font-size: 13.5px;
    color: var(--text-dark);
  }
  .contact-group {
    padding: 6px 0 8px;
    border-bottom: 1px solid var(--rule);
  }
  .contact-line {
    display: flex;
    align-items: center;
    gap: 10px;
    height: 20px;
  }
  .contact-line svg { width: 12px; height: 12px; flex: none; fill: var(--text-dark); }
  .licence {
    position: absolute;
    right: 28px;
    bottom: 22px;
    font-size: 13px;
    color: var(--text-dark);
  }
</style>
</head>
<body>

<section class="card card--back" aria-label="Card back">
  <div class="brand">
    <div class="brand-square"></div>
    <div class="brand-name">Bracken Hollow<br>Masonry</div>
  </div>
</section>

<section class="card card--front" aria-label="Card front">
  <div class="faint-mark"></div>

  <div class="brand">
    <div class="brand-square"></div>
    <div class="brand-name">Bracken Hollow<br>Masonry</div>
  </div>

  <ul class="contact">
    <li class="contact-group">
      <div class="contact-line">
        <svg viewBox="0 0 12 12"><rect x="1" y="1" width="10" height="10" rx="1.5"/><rect x="3" y="3" width="6" height="2" fill="#f4f6f7"/></svg>
        <span>1300 517 926</span>
      </div>
      <div class="contact-line">
        <svg viewBox="0 0 12 12"><rect x="1" y="1" width="10" height="10" rx="1"/><rect x="3" y="2.5" width="6" height="3" fill="#f4f6f7"/></svg>
        <span>1900 457 618</span>
      </div>
      <div class="contact-line">
        <svg viewBox="0 0 12 12"><rect x="3" y="0.5" width="6" height="11" rx="1.2"/><rect x="4" y="2" width="4" height="7" fill="#f4f6f7"/></svg>
        <span>0471 926 038</span>
      </div>
    </li>
    <li class="contact-group">
      <div class="contact-line">
        <svg viewBox="0 0 12 12"><rect x="0.5" y="2" width="11" height="8" rx="1"/><path d="M1 2.5 L6 6.5 L11 2.5" stroke="#f4f6f7" stroke-width="1.2" fill="none"/></svg>
        <span>delwyn@brackenhollowmasonry.com.au</span>
      </div>
      <div class="contact-line">
        <svg viewBox="0 0 12 12"><circle cx="6" cy="6" r="5.2" fill="none" stroke="#2b2424" stroke-width="1.2"/><ellipse cx="6" cy="6" rx="2.2" ry="5.2" fill="none" stroke="#2b2424" stroke-width="1"/><line x1="0.8" y1="6" x2="11.2" y2="6" stroke="#2b2424" stroke-width="1"/></svg>
        <span>www.brackenhollowmasonry.com.au</span>
      </div>
    </li>
    <li class="contact-group">
      <div class="contact-line">
        <svg viewBox="0 0 12 12"><path d="M6 0.5 C3.5 0.5 2 2.3 2 4.4 C2 7.2 6 11.5 6 11.5 C6 11.5 10 7.2 10 4.4 C10 2.3 8.5 0.5 6 0.5 Z"/><circle cx="6" cy="4.4" r="1.5" fill="#f4f6f7"/></svg>
        <span>518/ 217 Wendlebury st Thornvale</span>
      </div>
    </li>
  </ul>

  <div class="licence">Lic nr: 847263k</div>
</section>

</body>
</html>
```